Romantic Comedy Film Needs a Cool Poster

Need a professional looking poster for our film called Gloria Wobbleknee. The film is a romantic comedy about a guy who makes himself allergic to his girlfriend. I'm not sure quite what I want the poster to look like but I've included a few images of Gloria (the main character) so do what you think would look best, even cutting the backgrounds out is encouraged if you have a good vision. It just has to say "Gloria Wobbleknee", and that can be in all caps or whatever you think looks best. I'm even open to not using any of the pictures if you can come up with a design that looks good. Note: I probably don't want to use the words "bang bang" in the poster as it will be too distracting, but if you think it would work go for it.
The film is black and white, so keep this in mind when making your poster design. The main inspiration for the film is another film called 'Mildred Ok'
The final poster file has to follow standard poster print spec and resolution requirements as we will be printing it large as well submitting the file to film festivals. If the images I've provided are too small to achieve this, just make them a little bigger, I don't mind too much if it looks good.
Any questions, just let me know. Thank you for your time! :)
Industry/Entity Type
Film Production
Font styles to use
Other font styles liked:
- No preference. Probably sans serif, but looking at the poster for the film Mildred Ok, Serif seems to work. Go with your judgement.
Colors
Designer to choose colors to be used in the design.
Requirements
Must have
- Must have the title Gloria Wobbleknee on the poster without any line break between the words "love" and "sick". Any capitalisation and font, but the only variation we don't want is "Gloria WobbleKnee" because "Lovesick" needs to be conveyed as one word.
Nice to have
- The actual film is entirely black and white, so keep this in mind with your designs. You might want to keep the poster entirely black and white, or even just duller colours. What could maybe work best is just one single colour in addition to the black and white. Search up the Mildred Ok poster to see an example of the one extra colour standing out. But I'm not against any colours or ideas.
- The tagline for the film is: His mind is telling him yes, but his body is telling him no.
- Only include this if you think it works well.
Should not have
- There must not be a line break between "love" and "sick".

```html
<!DOCTYPE html>
<html lang="en">
<head>
<meta charset="utf-8">
<title>Gloria Wobbleknee — Poster</title>
<link rel="stylesheet" href="https://fonts.googleapis.com/css2?family=Anton&family=Architects+Daughter&family=Oswald:wght@500&display=swap">
<style>
  :root {
    --paper: #f4f4f2;
    --paper-shade: #e2e2df;
    --ink: #0d0d0d;
    --yellow: #ffd200;
    --gold: #c9a52a;
    --white: #ffffff;
  }
  html, body { margin: 0; padding: 0; overflow: hidden; }
  .poster {
    position: relative;
    width: 800px;
    height: 1200px;
    overflow: hidden;
    background: radial-gradient(ellipse at 40% 35%, var(--paper) 0%, #ebebe8 60%, var(--paper-shade) 100%);
  }
  .poster svg.layer { position: absolute; inset: 0; }
  .title-text {
    font-family: "Anton", sans-serif;
    fill: var(--yellow);
  }
  .title-shadow { fill: var(--white); }
  .tagline {
    position: absolute;
    left: 72px;
    top: 398px;
    width: 650px;
    margin: 0;
    font-family: "Architects Daughter", cursive;
    font-size: 19px;
    letter-spacing: 1.5px;
    text-transform: uppercase;
    color: var(--ink);
    transform: rotate(-2.6deg);
    white-space: nowrap;
  }
  .credits {
    position: absolute;
    left: 0;
    top: 1048px;
    width: 800px;
    font-family: "Oswald", sans-serif;
    color: var(--gold);
    text-transform: uppercase;
  }
  .credit-row {
    display: flex;
    justify-content: center;
    align-items: center;
    gap: 9px;
    height: 34px;
  }
  .credit { display: flex; align-items: center; gap: 4px; }
  .credit-role {
    font-size: 7.5px;
    line-height: 7px;
    text-align: right;
    letter-spacing: 0.2px;
  }
  .credit-name {
    font-size: 21px;
    letter-spacing: -0.3px;
    transform: scaleX(0.82);
    transform-origin: left center;
    margin-right: -14px;
    white-space: nowrap;
  }
</style>
</head>
<body>
<main class="poster">
  <svg class="layer" width="800" height="1200" viewBox="0 0 800 1200" aria-hidden="false">
    <!-- title banner -->
    <polygon class="title-banner" fill="var(--ink)"
      points="118,98 616,52 626,176 724,186 718,366 92,380 84,226 130,222"/>
    <g transform="rotate(-3 400 220)">
      <text class="title-text title-shadow" x="181" y="205" font-size="142" textLength="420" lengthAdjust="spacingAndGlyphs">GLORIA</text>
      <text class="title-text" x="175" y="199" font-size="142" textLength="420" lengthAdjust="spacingAndGlyphs">GLORIA</text>
      <text class="title-text title-shadow" x="113" y="362" font-size="150" textLength="596" lengthAdjust="spacingAndGlyphs">WOBBLEKNEE</text>
      <text class="title-text" x="107" y="356" font-size="150" textLength="596" lengthAdjust="spacingAndGlyphs">WOBBLEKNEE</text>
    </g>

    <!-- portrait with yellow offset backing -->
    <polygon class="portrait-backing" fill="var(--yellow)"
      points="230,480 300,452 420,436 520,470 560,560 570,760 640,790 690,860 680,1000 70,1004 84,900 150,830 235,780 250,650"/>
    <polygon class="portrait" role="img"
      aria-label="Black and white cut-out photo of the lead actor with tissue in his nose, glancing sideways, surrounded by hand-drawn yellow YES and NO speech bubbles and a heart doodle"
      fill="url(#portraitTone)"
      points="262,494 330,462 440,452 540,490 556,580 562,770 640,800 690,870 692,1004 100,1004 104,910 170,850 272,800 268,650"/>
    <defs>
      <linearGradient id="portraitTone" x1="0" y1="0" x2="0" y2="1">
        <stop offset="0" stop-color="#2a2a2a"/>
        <stop offset="0.35" stop-color="#8c8c8c"/>
        <stop offset="0.6" stop-color="#3a3a3a"/>
        <stop offset="1" stop-color="#111111"/>
      </linearGradient>
    </defs>

    <!-- credits band -->
    <polygon class="credits-rule" fill="var(--yellow)" points="0,1002 800,1010 800,1024 0,1016"/>
    <polygon class="credits-band" fill="var(--ink)" points="0,1012 800,1020 800,1160 0,1168"/>
  </svg>

  <p class="tagline">His mind is telling him yes, but his body is telling him no</p>

  <section class="credits">
    <div class="credit-row">
      <span class="credit"><span class="credit-role">Starring</span><span class="credit-name">Owen Marsh</span></span>
      <span class="credit"><span class="credit-name">Tess Delaney</span></span>
      <span class="credit"><span class="credit-name">Felix Brandt</span></span>
      <span class="credit"><span class="credit-role">Edited<br>by</span><span class="credit-name">Milo Santoro</span></span>
    </div>
    <div class="credit-row">
      <span class="credit"><span class="credit-role">Music<br>by</span><span class="credit-name">Ren Ho Tan</span></span>
      <span class="credit"><span class="credit-role">Sound<br>designer</span><span class="credit-name">Aiden Russo</span></span>
      <span class="credit"><span class="credit-role">Production<br>designer</span><span class="credit-name">Nadia Fowler</span></span>
      <span class="credit"><span class="credit-role">Director of<br>photography</span><span class="credit-name">Lena Park</span></span>
    </div>
    <div class="credit-row">
      <span class="credit"><span class="credit-role">Produced<br>by</span><span class="credit-name">Daniel Whitcombe</span></span>
      <span class="credit"><span class="credit-name">Ivy Pemberton</span></span>
      <span class="credit"><span class="credit-role">Written and<br>directed by</span><span class="credit-name">Owen Marsh</span></span>
    </div>
  </section>
</main>
</body>
</html>
```